Celebrating 10 Years

advertisement for print magazine
also to be used on email.
Updates

The relevant information I need (beside my photo and the firm logo) is:
my name: Tom Harlowe
Circuit Civil Mediator
the 800 telephone number provided
reference to the 10 years (new design)
and the words:
Thank You.

Target Market(s)

clients

Industry/Entity Type

Mediation Legal

Font styles to use
Sans Serif

Colors
0054AA
0677BA
7BADD7
CADEEF
E8F1F8
FFF300
FFF600
FEFA6F
FFFEC7
FFFEE8

```html
<!DOCTYPE html>
<html lang="en">
<head>
<meta charset="utf-8">
<title>Tom Harlowe – Circuit Civil Mediator – Celebrating 10 Years</title>
<link href="https://fonts.googleapis.com/css2?family=Poppins:wght@400;600;700&display=swap" rel="stylesheet">
<style>
  :root {
    --blue-deep: #0054aa;
    --blue-mid: #0677ba;
    --blue-soft: #7badd7;
    --blue-pale: #cadeef;
    --blue-mist: #e8f1f8;
    --yellow: #fff300;
    --yellow-bright: #fff600;
    --yellow-soft: #fefa6f;
    --yellow-cream: #fffec7;
    --yellow-mist: #fffee8;
    --ink: #10233f;
    --white: #ffffff;
  }
  html, body { margin: 0; padding: 0; overflow: hidden; }
  body { width: 1200px; height: 826px; background: var(--white); font-family: 'Poppins', sans-serif; }
  .ad { position: relative; width: 1200px; height: 826px; overflow: hidden; background: var(--white); }

  .office-backdrop {
    position: absolute; left: 14px; top: 12px; width: 1172px; height: 800px;
    background: linear-gradient(180deg, var(--yellow-mist) 0%, var(--blue-mist) 35%, var(--blue-pale) 100%);
  }
  .portrait {
    position: absolute; left: 0; top: 0; width: 690px; height: 660px;
    background: linear-gradient(180deg, rgba(202,222,239,0.4) 0%, #d7c7bd 30%, #cdb6a8 50%, #23407a 68%, #1b3166 100%);
    clip-path: polygon(24% 2%, 76% 2%, 78% 52%, 100% 62%, 100% 100%, 0 100%, 0 66%, 26% 54%);
  }

  .firm { position: absolute; left: 668px; top: 62px; display: flex; align-items: center; gap: 20px; }
  .firm-mark { width: 110px; height: 110px; border-radius: 50%; background: var(--blue-deep); }
  .firm-name { margin: 0; color: var(--blue-deep); font-weight: 600; font-size: 25px; line-height: 32px; letter-spacing: 2px; text-transform: uppercase; }

  .headline-band {
    position: absolute; left: 402px; top: 213px; width: 782px; height: 146px;
    background: linear-gradient(90deg, var(--blue-deep) 0%, var(--blue-deep) 60%, var(--blue-mid) 100%);
  }
  .anniversary {
    position: absolute; left: 402px; top: 226px; width: 782px; margin: 0; text-align: center;
    color: var(--yellow-cream); font-weight: 600; font-size: 22px; line-height: 30px; letter-spacing: 6px;
  }
  .headline {
    position: absolute; left: 402px; top: 250px; width: 782px; margin: 0; text-align: center;
    font-weight: 700; font-size: 76px; line-height: 96px; letter-spacing: -1px; color: var(--yellow);
  }

  .label-strip {
    position: absolute; left: 765px; width: 260px; height: 48px;
    background: linear-gradient(90deg, rgba(0,84,170,0) 0%, var(--blue-deep) 25%, var(--blue-deep) 75%, rgba(0,84,170,0) 100%);
    color: var(--white); font-weight: 700; font-size: 25px; line-height: 48px; text-align: center;
  }
  .label-email { top: 384px; }
  .label-phone { top: 612px; z-index: 2; }

  .email-bar {
    position: absolute; right: 16px; height: 73px; box-sizing: border-box;
    background: linear-gradient(90deg, var(--yellow-soft) 0%, var(--yellow-soft) 35%, var(--yellow-cream) 100%);
    color: var(--ink); font-size: 29px; line-height: 73px; padding-right: 100px; text-align: right;
  }
  .email-work { top: 430px; width: 684px; }
  .email-personal { top: 512px; width: 524px; }

  .phone-panel { position: absolute; left: 0; top: 0; width: 1200px; height: 826px; }
  .name-panel {
    position: absolute; left: 0; top: 658px; width: 620px; height: 168px;
    background: var(--blue-deep);
    clip-path: polygon(0 0, 95% 0, 82.5% 100%, 0 100%);
  }
  .name { position: absolute; left: 64px; top: 688px; margin: 0; color: var(--white); font-weight: 700; font-size: 56px; line-height: 72px; letter-spacing: -1px; }
  .role { position: absolute; left: 67px; top: 756px; margin: 0; color: var(--yellow); font-weight: 400; font-size: 23px; line-height: 30px; letter-spacing: 5px; }
  .phone { position: absolute; left: 626px; top: 686px; margin: 0; color: var(--ink); font-weight: 700; font-size: 70px; line-height: 90px; letter-spacing: -1px; }
</style>
</head>
<body>
<div class="ad">
  <div class="office-backdrop" role="img" aria-label="Blurred bright office with people in the background"></div>
  <div class="portrait" role="img" aria-label="Portrait photo of Tom Harlowe in a navy suit and striped tie"></div>

  <div class="firm">
    <div class="firm-mark"></div>
    <p class="firm-name">Harbor Point<br>Mediation Group</p>
  </div>

  <div class="headline-band"></div>
  <p class="anniversary">CELEBRATING 10 YEARS</p>
  <h2 class="headline">THANK YOU!</h2>

  <div class="label-strip label-email">EMAIL:</div>
  <div class="email-bar email-work">Tharlowe@hpm-adr.com</div>
  <div class="email-bar email-personal">Tomharlowe@mailbox.com</div>

  <svg class="phone-panel" viewBox="0 0 1200 826" aria-hidden="true">
    <polygon points="605,633 1200,633 1200,826 511,826" fill="#fff300"/>
  </svg>
  <div class="name-panel"></div>
  <div class="label-strip label-phone">PHONE:</div>

  <h1 class="name">TOM HARLOWE</h1>
  <p class="role">CIRCUIT CIVIL MEDIATOR</p>
  <p class="phone">(800) 555 0142</p>
</div>
</body>
</html>
```